Packaging Design for Boneless Picnic Ham

We are Tidewell Provisions Limited, a company based in Trinidad which is located within the Caribbean. We produce and sell a plethora of meat products including a variety of hams, sausages and even bacon.

We require a packaging design for a ham product. This product is packaged within a cryovac (11" X 18") shrink bag which would be used to package our Boneless Picnic Ham which weighs 2.5 Kilograms.

The design space should be 7 inches wide and 6 inches in height. The design is 3 inches from the bottom and 2 inches off each side.

Our target audience comprises of caterers as well as the average household folk. What sets our product apart is that it is has a great taste, 20% less salt and is affordable and easy. We commonly refer to it as the "Sunday Roast Joint".

Attached below, is our logo which you must incorporate onto the design. We also request that the header be "Hickory Smoked Boneless Picnic Ham".

Target Market(s)

Caterers and Average Household Folk

Font styles to use
Sans Serif

Requirements
Must have
• The Tidewell Provisions Company Logo and the header must have "Hickory Smoked Boneless Picnic Ham"
Nice to have
• Maximum Creativity
Should not have
• No animal artwork should be included onto the design

```html
<!DOCTYPE html>
<html lang="en">
<head>
<meta charset="utf-8">
<title>Tidewell Provisions – Hickory Smoked Boneless Picnic Ham</title>
<link rel="stylesheet" href="https://fonts.googleapis.com/css2?family=Titan+One&family=Rubik:wght@500;700;800&family=Tinos&family=Lobster&display=swap">
<style>
  :root {
    --page: #ffffff;
    --sky-top: #86dbe8;
    --sky-bottom: #f4fbfc;
    --band-purple: #5a2c86;
    --band-magenta: #c0175a;
    --band-red: #d4143f;
    --ribbon-yellow: #f6dc78;
    --brand-blue: #1f3f9a;
    --navy: #1b1f4d;
    --maroon: #8e1b1b;
    --sun-yellow: #f7ee1a;
    --ink: #111111;
    --white: #ffffff;
    --photo-pink: #d98d8f;
    --photo-rose: #b4575e;
    --photo-green: #4c7a3a;
  }
  html, body {
    margin: 0;
    padding: 0;
    width: 1200px;
    height: 1054px;
    overflow: hidden;
    background: var(--page);
  }
  .label {
    display: block;
    width: 1200px;
    height: 1054px;
  }
  .brand-name { font-family: "Rubik", sans-serif; font-weight: 800; fill: var(--brand-blue); }
  .tagline { font-family: "Tinos", serif; fill: var(--maroon); }
  .callout { font-family: "Rubik", sans-serif; font-weight: 800; fill: var(--sun-yellow); stroke: var(--ink); stroke-width: 6; paint-order: stroke; stroke-linejoin: round; }
  .title-main { font-family: "Titan One", sans-serif; fill: var(--white); stroke: var(--navy); stroke-width: 8; paint-order: stroke; stroke-linejoin: round; }
  .title-sub { font-family: "Titan One", sans-serif; fill: var(--sun-yellow); stroke: var(--navy); stroke-width: 5; paint-order: stroke; stroke-linejoin: round; }
  .title-script { font-family: "Lobster", cursive; fill: var(--maroon); stroke: var(--white); stroke-width: 6; paint-order: stroke; stroke-linejoin: round; }
  .salt-percent { font-family: "Rubik", sans-serif; font-weight: 800; fill: var(--sun-yellow); stroke: var(--ink); stroke-width: 3; paint-order: stroke; }
  .salt-words { font-family: "Rubik", sans-serif; font-weight: 700; fill: var(--brand-blue); }
  .weight-text { font-family: "Rubik", sans-serif; font-weight: 500; fill: var(--white); }
</style>
</head>
<body>
<svg class="label" viewBox="0 0 1200 1054" xmlns="http://www.w3.org/2000/svg">
  <defs>
    <linearGradient id="sky" x1="0" y1="0" x2="1" y2="1">
      <stop offset="0" stop-color="var(--sky-top)"/>
      <stop offset="0.6" stop-color="var(--sky-bottom)"/>
    </linearGradient>
    <linearGradient id="band" x1="0" y1="0" x2="0" y2="1">
      <stop offset="0" stop-color="var(--band-purple)"/>
      <stop offset="0.55" stop-color="var(--band-magenta)"/>
      <stop offset="1" stop-color="var(--band-red)"/>
    </linearGradient>
    <radialGradient id="ham" cx="0.45" cy="0.45" r="0.6">
      <stop offset="0" stop-color="var(--photo-pink)"/>
      <stop offset="0.6" stop-color="var(--photo-rose)"/>
      <stop offset="1" stop-color="var(--photo-green)"/>
    </radialGradient>
    <clipPath id="label-area">
      <rect x="120" y="110" width="962" height="822"/>
    </clipPath>
  </defs>

  <g clip-path="url(#label-area)">
    <rect class="sky" x="120" y="110" width="962" height="822" fill="url(#sky)"/>
    <path class="band" d="M120 452 C 360 400, 600 420, 820 380 S 1040 340, 1082 349 L1082 932 L120 932 Z" fill="url(#band)"/>
    <circle class="serving-photo" cx="808" cy="767" r="425" fill="url(#ham)" stroke="var(--white)" stroke-width="8"
            role="img" aria-label="Photo of sliced glazed hickory smoked ham with pineapple rings, cherries and parsley"/>
  </g>

  <polygon class="brand-ribbon" points="165,253 425,130 747,288 493,411" fill="var(--ribbon-yellow)"
           role="img" aria-label="Yellow woven ribbon behind the brand name"/>
  <text class="brand-name" x="473" y="268" font-size="52" text-anchor="middle">Tidewell</text>
  <text class="brand-name" x="473" y="324" font-size="52" text-anchor="middle">Provisions</text>

  <text class="tagline" x="897" y="220" font-size="62" text-anchor="middle">GREAT</text>
  <text class="tagline" x="897" y="302" font-size="62" text-anchor="middle">TASTE</text>

  <text class="callout" x="884" y="434" font-size="74" text-anchor="middle">Sunday</text>
  <text class="callout" x="884" y="514" font-size="74" text-anchor="middle">Roast</text>
  <text class="callout" x="884" y="598" font-size="74" text-anchor="middle">Joint</text>

  <text class="title-main" x="162" y="555" font-size="100" textLength="441" lengthAdjust="spacingAndGlyphs">HICKORY</text>
  <text class="title-sub" x="167" y="627" font-size="44" textLength="436" lengthAdjust="spacingAndGlyphs">Smoked Boneless</text>
  <text class="title-script" x="162" y="719" font-size="92" textLength="475" lengthAdjust="spacingAndGlyphs">Picnic Ham</text>

  <g class="salt-badge">
    <circle cx="253" cy="836" r="82" fill="var(--white)" stroke="var(--brand-blue)" stroke-width="9"/>
    <text class="salt-percent" x="253" y="823" font-size="44" text-anchor="middle">20%</text>
    <text class="salt-words" x="253" y="856" font-size="30" text-anchor="middle">LESS</text>
    <text class="salt-words" x="253" y="888" font-size="30" text-anchor="middle">SALT</text>
  </g>

  <g class="weight-badge">
    <ellipse cx="962" cy="870" rx="80" ry="44" fill="var(--ink)"/>
    <text class="weight-text" x="962" y="864" font-size="22" text-anchor="middle">WEIGHT</text>
    <text class="weight-text" x="968" y="890" font-size="22" text-anchor="middle">25 Kg.</text>
  </g>
</svg>
</body>
</html>
```